HM Marketing Piece

Heron Meadow was created in 1984 as a shared aircraft ownership comprised of individual stockholders, interested in sharing the cost of aircraft ownership. Our strategy is simple, make owning and flying well maintained and upgraded aircraft more affordable through shared ownership.

When you own an aircraft individually, you have all the costs of a loan, hangar, insurance, subscriptions, annual inspection, and those unscheduled maintenance issues.

When you rent an aircraft from a local FBO, you get well used, dirty aircraft that everyone abuses with minimum hour requirements for weekend getaways that turn a 2 hour trip into a 9 hour hit on your wallet.

The solution? Shared aircraft ownership. Heron Meadow has three aircraft based out of Bramwell Field (KQLP). When you join a partnership, you split fixed costs between multiple individuals, AND get access to multiple well maintained and upgraded aircraft. When you fly, you pay the variable costs of your flight time only. Dividing the fixed expenses among multiple members makes flying much more affordable.

Benefits of shared aircraft ownership:

• Much cheaper than owning an aircraft individually
• Access to multiple aircraft
• Higher quality aircraft than your local FBO

• Hangared aircraft, flown by owners, not renters
• No overnight minimums
• On-line scheduling

www.heronmeadowfly.example

```html
<!DOCTYPE html>
<html lang="en">
<head>
<meta charset="utf-8">
<title>Heron Meadow – Shared Aircraft Ownership</title>
<link rel="stylesheet" href="https://fonts.googleapis.com/css2?family=Nunito:wght@800&family=Questrial&display=swap">
<style>
  :root {
    --paper: #ffffff;
    --ink: #1d1d1f;
    --brand-blue: #1f6fb2;
    --brand-navy: #1e2f73;
  }
  * { margin: 0; padding: 0; box-sizing: border-box; }
  html, body { width: 1200px; height: 930px; overflow: hidden; background: var(--paper); }
  .piece {
    position: relative;
    width: 1200px;
    height: 930px;
    background: var(--paper);
    font-family: "Questrial", sans-serif;
    color: var(--ink);
  }
  .fleet-photo {
    position: absolute;
    left: 0;
    width: 266px;
  }
  .fleet-photo--top {
    top: 0; height: 254px;
    background: linear-gradient(to bottom, #9fc3e6 0%, #c9dbe8 38%, #8f9497 60%, #6b6e71 100%);
  }
  .fleet-photo--middle {
    top: 266px; height: 234px;
    background: linear-gradient(to bottom, #4f8bcf 0%, #86b2de 38%, #3f5b33 50%, #7c7f80 62%, #5f6264 100%);
  }
  .fleet-photo--bottom {
    top: 514px; height: 250px;
    background: linear-gradient(to bottom, #3d7bc4 0%, #86b4e0 38%, #5a6a55 50%, #4d5053 64%, #3f4245 100%);
  }
  .benefits {
    position: absolute;
    left: 310px;
    top: 88px;
    width: 320px;
  }
  .benefits__title {
    font-family: "Nunito", sans-serif;
    font-weight: 800;
    font-size: 30.5px;
    line-height: 27px;
    color: var(--brand-blue);
    letter-spacing: -0.3px;
  }
  .benefits__list {
    list-style: none;
    margin-top: 14px;
  }
  .benefits__item {
    position: relative;
    padding-left: 12px;
    font-size: 25.5px;
    line-height: 26.5px;
    margin-bottom: 11px;
    white-space: nowrap;
  }
  .benefits__item::before {
    content: "";
    position: absolute;
    left: 0;
    top: 12px;
    width: 3px;
    height: 3px;
    border-radius: 50%;
    background: var(--ink);
  }
  .brand {
    position: absolute;
    left: 310px;
    top: 600px;
  }
  .brand__name {
    font-size: 50px;
    line-height: 54px;
    color: var(--brand-navy);
  }
  .brand__web {
    margin-top: 48px;
    font-size: 25.5px;
    line-height: 30px;
  }
  .brand__phone {
    margin-top: 5px;
    font-family: "Nunito", sans-serif;
    font-weight: 800;
    font-size: 27px;
    line-height: 30px;
    color: var(--brand-blue);
  }
</style>
</head>
<body>
<main class="piece">
  <div class="fleet-photo fleet-photo--top" role="img" aria-label="Photo of a white low-wing club aircraft parked on the ramp"></div>
  <div class="fleet-photo fleet-photo--middle" role="img" aria-label="Photo of a white and blue low-wing club aircraft on the apron"></div>
  <div class="fleet-photo fleet-photo--bottom" role="img" aria-label="Photo of a white high-wing club aircraft on the tarmac"></div>

  <section class="benefits">
    <h1 class="benefits__title">Benefits of shared<br>aircraft ownership:</h1>
    <ul class="benefits__list">
      <li class="benefits__item">Much cheaper than<br>owning an aircraft<br>individually</li>
      <li class="benefits__item">Access to multiple<br>aircraft</li>
      <li class="benefits__item">Higher quality aircraft<br>than your local FBO</li>
      <li class="benefits__item">Hangared aircraft,<br>flown by owners, not<br>renters</li>
      <li class="benefits__item">No overnight minimums</li>
      <li class="benefits__item">On-line scheduling</li>
    </ul>
  </section>

  <footer class="brand">
    <div class="brand__name">Heron Meadow</div>
    <div class="brand__web">heronmeadowfly.example</div>
    <div class="brand__phone">Ph. 555.014.2273</div>
  </footer>
</main>
</body>
</html>
```